Ferncrest Dental, LLC business card project

Business card to be designed with current logo.
Dental office- please keep design of card that looks clean and professional.
Please include the following info:
Ferncrest Dental, LLC
Dr. Lorna Pettigrew
2871 Marlowe Street
Bethlehem, PA 18093
610-555-0193
ferncrestdental.office@examplemail.test
Hello everyone-
Reason: Just got back from overseas- will look at all designs and provide feedback. Thank you!
Reason: Polling my friends for the final selection-
thank you to all those that participated- so many talented designers!

```html
<!DOCTYPE html>
<html lang="en">
<head>
<meta charset="utf-8">
<title>Ferncrest Dental – Business Card</title>
<link rel="stylesheet" href="https://fonts.googleapis.com/css2?family=Questrial&family=Libre+Baskerville:wght@700&display=swap">
<style>
  :root {
    --backdrop: #1d2b3b;
    --card-white: #ffffff;
    --brand-green: #6aa33a;
    --name-green: #4f8f3c;
    --lime: #b0d133;
    --forest: #2c5220;
    --band-edge: #1f3d17;
    --ink: #1e2a14;
    --tooth-light: #f7f7f7;
    --tooth-shade: #d2d4d6;
  }
  * { margin: 0; padding: 0; box-sizing: border-box; }
  html, body {
    width: 1200px;
    height: 1000px;
    overflow: hidden;
    background: var(--backdrop);
  }
  .business-card {
    position: absolute;
    left: 75px;
    top: 201px;
    width: 1050px;
    height: 598px;
    background: var(--card-white);
    overflow: hidden;
    box-shadow: 0 10px 30px rgba(0, 0, 0, 0.35);
  }
  .green-band {
    position: absolute;
    inset: 0;
    width: 1050px;
    height: 598px;
  }
  .tooth-illustration {
    position: absolute;
    left: 654px;
    top: 74px;
    width: 363px;
    height: 389px;
    border-radius: 46% 46% 40% 40%;
    background: radial-gradient(ellipse at 45% 35%, var(--tooth-light) 0%, #ebecee 55%, var(--tooth-shade) 100%);
  }
  .brand {
    position: absolute;
    left: 120px;
    top: 132px;
    display: flex;
    align-items: center;
    gap: 26px;
  }
  .brand-mark {
    width: 86px;
    height: 86px;
    border-radius: 50%;
    background: var(--lime);
  }
  .brand-name {
    font-family: "Questrial", "Century Gothic", sans-serif;
    font-size: 78px;
    font-weight: 400;
    line-height: 1;
    color: var(--brand-green);
    letter-spacing: -1px;
    white-space: nowrap;
  }
  .doctor-name {
    position: absolute;
    left: 103px;
    top: 256px;
    font-family: "Libre Baskerville", "Times New Roman", serif;
    font-weight: 700;
    font-size: 34px;
    color: var(--name-green);
    letter-spacing: 0.5px;
  }
  .contact {
    position: absolute;
    left: 30px;
    top: 433px;
    display: grid;
    grid-template-columns: 147px auto;
    column-gap: 10px;
    row-gap: 5px;
    font-family: "Questrial", "Century Gothic", sans-serif;
    font-size: 26px;
    line-height: 30px;
    color: var(--ink);
  }
  .contact dt { text-align: right; }
</style>
</head>
<body>
  <article class="business-card">
    <svg class="green-band" viewBox="0 0 1050 598" aria-hidden="true">
      <defs>
        <linearGradient id="bandGradient" x1="0" y1="1" x2="1" y2="0">
          <stop offset="0" stop-color="#b0d133"/>
          <stop offset="0.45" stop-color="#7ea52c"/>
          <stop offset="1" stop-color="#2c5220"/>
        </linearGradient>
      </defs>
      <path d="M0 392 C 260 372 620 338 1050 282 L1050 598 L0 598 Z" fill="#1f3d17"/>
      <path d="M0 400 C 260 384 620 352 1050 298 L1050 598 L0 598 Z" fill="url(#bandGradient)"/>
    </svg>

    <div class="tooth-illustration" role="img" aria-label="Glossy white 3D molar tooth standing on a white oval base"></div>

    <header class="brand">
      <span class="brand-mark" aria-hidden="true"></span>
      <h1 class="brand-name">Ferncrest Dental</h1>
    </header>

    <p class="doctor-name">Dr. Lorna Pettigrew</p>

    <dl class="contact">
      <dt>Address:</dt>
      <dd>2871 Marlowe Street<br>Bethlehem, PA 18093</dd>
      <dt>Tel:</dt>
      <dd>610-555-0193</dd>
      <dt>E-Mail:</dt>
      <dd>ferncrestdental.office@examplemail.test</dd>
    </dl>
  </article>
</body>
</html>
```